Austrian finance und insurance broker needs business card design

We Need a serious looking Design for Business Card. we consult private and corporates customers in finance and insurance questions. the final design should express security and experience. We consult customers in questions of loans, Investments and insurance and have a wide range of Banks to offer. We compare several offers and select the best for our customers.

Target Market(s)

private and coporate customers with efforts in Money and insurance

Industry/Entity Type

Insurance Broker

Contact Information for Business Card

Martin Brauneder
Geschäftsführer
staatl. geprüfter Vermögensberater und Versicherungsmakler
Tel: 0664 512 8049
office@der-brauneder.at
www.der-brauneder.at
Anton Weibl Gasse 14
2135 Halbach
GISA Nr. 40527318 u. 40816493 (backside)

Font styles to use
Serif
Sans Serif

Requirements
Must have
• logo (designcrowd zip) and all Details
Nice to have
• makler logo design, maybe a 2 coloured Version is possible

```html
<!DOCTYPE html>
<html lang="de">
<head>
<meta charset="utf-8">
<title>Brauneder Vermögensberatung – Visitenkarte</title>
<link href="https://fonts.googleapis.com/css2?family=Poppins:wght@400;500;600;700&family=Roboto:wght@400;500&display=swap" rel="stylesheet">
<style>
  :root {
    --page: #d9d9db;
    --card: #27282b;
    --card-deep: #1c1d1f;
    --emboss: #3a3b3f;
    --emboss-text: #4b4c51;
    --blue: #1172bf;
    --blue-light: #2a8ad6;
    --grey: #6a6c71;
    --white: #ffffff;
    --seal: #c8202a;
  }
  * { margin: 0; padding: 0; box-sizing: border-box; }
  html, body {
    width: 799px; height: 1200px; overflow: hidden;
    background: var(--page);
  }
  .canvas {
    position: relative; width: 799px; height: 1200px;
  }
  .card {
    position: absolute; left: 80px; width: 640px; height: 370px;
    border-radius: 22px; overflow: hidden;
    background: var(--card);
    font-family: "Poppins", sans-serif;
    box-shadow: 0 8px 24px rgba(0,0,0,.25);
  }
  .card--front { top: 150px; }
  .card--back { top: 680px; }

  /* front */
  .front-edge {
    position: absolute; left: 0; right: 0; bottom: 0; height: 10px;
    background: linear-gradient(90deg, var(--blue) 0 50%, var(--grey) 50% 100%);
  }
  .front-brand {
    position: absolute; left: 0; right: 0; top: 118px;
    text-align: center; color: var(--emboss-text);
  }
  .front-brand__name { font-size: 26px; font-weight: 500; letter-spacing: .3px; }
  .front-brand__tagline { font-size: 17px; margin-top: 4px; letter-spacing: .5px; }
  .front-registry {
    position: absolute; left: 0; right: 0; bottom: 42px; text-align: center;
    font-family: "Roboto", sans-serif; font-size: 16px; color: var(--grey);
    letter-spacing: 1px;
  }

  /* back */
  .back-waves { position: absolute; inset: 0; }
  .back-brand { position: absolute; left: 36px; top: 92px; }
  .back-brand__name {
    color: var(--blue-light); font-size: 21px; font-weight: 600; line-height: 1.2;
  }
  .back-brand__tagline { color: var(--white); font-size: 14px; margin-top: 4px; }
  .person { position: absolute; right: 36px; top: 70px; text-align: right; }
  .person__name { color: var(--blue-light); font-size: 25px; font-weight: 700; }
  .person__role {
    color: var(--white); font-family: "Roboto", sans-serif;
    font-size: 14px; line-height: 1.35; margin-top: 4px;
  }
  .partner-seal {
    position: absolute; right: 250px; top: 170px;
    width: 34px; height: 34px; border-radius: 50%; background: var(--seal);
  }
  .contact {
    position: absolute; right: 28px; top: 248px; list-style: none;
    font-family: "Roboto", sans-serif; color: var(--white);
    font-size: 17px; line-height: 26px; text-align: right;
  }
  .contact li { display: flex; justify-content: flex-end; align-items: center; gap: 12px; }
  .contact svg { width: 16px; height: 16px; fill: var(--white); }
  .contact .spacer { width: 16px; }
</style>
</head>
<body>
<div class="canvas">

  <section class="card card--front">
    <div class="front-brand">
      <div class="front-brand__name">Brauneder Vermögensberatung GmbH</div>
      <div class="front-brand__tagline">Finanzieren, Versichern, Vorsorgen</div>
    </div>
    <div class="front-registry">GISA Nr. 40527318 u. 40816493</div>
    <div class="front-edge"></div>
  </section>

  <section class="card card--back">
    <svg class="back-waves" viewBox="0 0 640 370" preserveAspectRatio="none">
      <path d="M0,170 C120,180 220,250 360,250 C480,250 560,215 640,200 L640,370 L0,370 Z" fill="var(--grey)"/>
      <path d="M0,190 C120,205 220,270 360,268 C480,266 560,230 640,218 L640,370 L0,370 Z" fill="var(--card-deep)"/>
      <path d="M0,212 C120,232 220,300 360,292 C470,286 550,245 640,236 L640,370 L0,370 Z" fill="var(--blue)"/>
    </svg>

    <div class="back-brand">
      <div class="back-brand__name">Brauneder<br>Vermögensberatung GmbH</div>
      <div class="back-brand__tagline">Finanzieren, Versichern, Vorsorgen</div>
    </div>

    <div class="person">
      <div class="person__name">Martin Brauneder</div>
      <div class="person__role">Geschäftsführer<br>Staatl. Geprüfter Vermögensberater<br>und Versicherungsmakler</div>
    </div>
    <div class="partner-seal"></div>

    <ul class="contact">
      <li>0664 512 8049
        <svg viewBox="0 0 24 24"><path d="M6.6 10.8a15 15 0 0 0 6.6 6.6l2.2-2.2c.3-.3.7-.4 1-.2 1.1.4 2.3.6 3.6.6.6 0 1 .4 1 1V20c0 .6-.4 1-1 1A17 17 0 0 1 3 4c0-.6.4-1 1-1h3.5c.6 0 1 .4 1 1 0 1.3.2 2.5.6 3.6.1.3 0 .7-.2 1z"/></svg></li>
      <li>office@der-brauneder.at
        <svg viewBox="0 0 24 24"><path d="M2 5h20v14H2z M4 7v.5l8 5 8-5V7l-8 5z" fill-rule="evenodd"/></svg></li>
      <li>www.der-brauneder.at
        <svg viewBox="0 0 24 24"><path d="M12 2a10 10 0 1 0 0 20 10 10 0 0 0 0-20zm0 2c1 1.2 1.8 3 2.1 5H9.9C10.2 7 11 5.2 12 4zM4.3 11h3.6a16 16 0 0 0 0 2H4.3a8 8 0 0 1 0-2zm5.6 0h4.2a14 14 0 0 1 0 2H9.9a14 14 0 0 1 0-2zm6.2 0h3.6a8 8 0 0 1 0 2h-3.6a16 16 0 0 0 0-2zM9.9 15h4.2c-.3 2-1.1 3.8-2.1 5-1-1.2-1.8-3-2.1-5z"/></svg></li>
      <li>Anton Weibl Gasse 14 2135 Halbach <span class="spacer"></span></li>
    </ul>
  </section>

</div>
</body>
</html>
```